Tend Your Garden - Keep your Spark - The freedom to choose and participate in your own path to hea

I have a logo that needs to be turned into a large banner for my website. I want to keep the same font in the uploaded logo image. Now this image could stay at the top of the header kind of where it is now on the web site, It doesn't have to be the main thing on the page. I want this header to be artistic - alive, healthy, joyous - colorful banner that shows wellness, healing, vitality and hope.
If you had a chronic illness and came to my site what would you want to see? You'd want to feel empowered, enlightened, engaged, hopeful and feel the love, right?.
I look forward to getting your creative ideas and designs.

Target Market(s)

People struggling with illness who are looking for a better quality of life. We provide training and education on how to do that. Hope, happiness - healing - Vitality - whole natural foods - mediation - visualization - whole health.

Industry/Entity Type

Health And Wellness

Logo Text

Tend Your Garden with the koru and with Harriet Bellamy (use the font on the uploaded file)

Requirements
Must have
• I've changed the photos in this order. You can pick up options here:
• https://www.filevorta.com/s/k7rptw2mzx/IMG_4471%20%20high%20resolution.jpg?dl=0
• https://www.filevorta.com/s/b3nqys8dlh/IMG_4529%20high%20resolution.jpg?dl=0
• My original logo - Tend Your Garden - Harriet Bellamy
• "Together we make tragic moments magic moments" Join us (sign up type button)
Nice to have
• Something stunningly simple, classy, inviting, where my message gets across.
• Here's a similar website to mine: http://dawnmelby.com
• I need a link to join up somewhere - with my quote.
• "My tragic moments have become magic moments" Join us (sign up type button)
Should not have
• I do not want other people in the header.
• No crunchy granola feel!
• This is gone mainstream now.

```html
<!DOCTYPE html>
<html lang="en">
<head>
<meta charset="utf-8">
<title>Tend Your Garden – Harriet Bellamy</title>
<link rel="stylesheet" href="https://fonts.googleapis.com/css2?family=Fredoka:wght@500;600&display=swap">
<style>
  :root {
    --slate: #3f5b58;
    --teal: #1fb3a4;
    --navy-text: #2a3f8f;
    --white: #ffffff;
    --join-blue: #2351a6;
    --logo-teal: #4fb3bd;
  }
  * { box-sizing: border-box; margin: 0; padding: 0; }
  html, body { width: 1200px; height: 440px; overflow: hidden; background: #ffffff; }

  .banner {
    position: relative;
    width: 1200px;
    height: 440px;
    overflow: hidden;
    font-family: "Fredoka", sans-serif;
  }

  .banner__backdrop {
    position: absolute;
    inset: 0;
    background:
      radial-gradient(ellipse 260px 220px at 930px 110px, rgba(255,255,255,0.95), rgba(255,255,255,0) 70%),
      radial-gradient(ellipse 260px 240px at 1110px 300px, rgba(255,250,245,0.9), rgba(255,255,255,0) 70%),
      radial-gradient(ellipse 380px 260px at 560px 300px, #e2471c, rgba(226,71,28,0) 75%),
      radial-gradient(ellipse 420px 240px at 360px 60px, #f5d94a, rgba(245,217,74,0) 75%),
      radial-gradient(ellipse 300px 260px at 760px 380px, #d9b0a8, rgba(217,176,168,0) 75%),
      linear-gradient(100deg, #f0b23c 0%, #ee8a3a 35%, #e7a07a 60%, #f3e3d6 80%, #f6ece4 100%);
  }

  .banner__portrait {
    position: absolute;
    left: 0;
    top: 0;
    width: 290px;
    height: 440px;
    background: linear-gradient(180deg, #c9a27f 0%, #c8dbe6 32%, #b4cddb 70%, #a9c3d3 100%);
    clip-path: polygon(0 0, 120px 0, 150px 130px, 270px 190px, 290px 440px, 0 440px);
  }

  .logo {
    position: absolute;
    top: 30px;
    left: 906px;
    display: flex;
    align-items: center;
    gap: 10px;
    color: var(--logo-teal);
    font-weight: 500;
    font-size: 23px;
    line-height: 1.15;
  }
  .logo__dot {
    width: 16px;
    height: 16px;
    border-radius: 50%;
    background: var(--logo-teal);
    margin-top: 30px;
  }

  .tagline {
    position: absolute;
    left: 300px;
    top: 135px;
    width: 360px;
    display: flex;
    flex-direction: column;
    gap: 6px;
    transform: rotate(-2deg);
  }
  .tagline__band {
    height: 56px;
    display: flex;
    align-items: center;
    padding-left: 22px;
    font-weight: 600;
    font-size: 30px;
    white-space: nowrap;
  }
  .tagline__band--slate { background: var(--slate); color: var(--white); }
  .tagline__band--teal { background: var(--teal); color: var(--navy-text); margin-left: 14px; }

  .join-button {
    position: absolute;
    left: 950px;
    top: 332px;
    width: 208px;
    height: 74px;
    display: flex;
    align-items: center;
    justify-content: center;
    color: var(--white);
    text-decoration: none;
    font-weight: 600;
    font-size: 31px;
  }
  .join-button svg { position: absolute; inset: 0; }
  .join-button span { position: relative; margin-left: -20px; }
</style>
</head>
<body>
  <header class="banner">
    <div class="banner__backdrop" role="img" aria-label="Soft glowing bokeh lights in yellow, orange and warm white"></div>
    <div class="banner__portrait" role="img" aria-label="Portrait photo of Harriet Bellamy in a light blue shirt"></div>

    <div class="logo">
      <span class="logo__dot"></span>
      <span>Tend Your Garden<br>Harriet Bellamy</span>
    </div>

    <div class="tagline">
      <div class="tagline__band tagline__band--slate">together we make</div>
      <div class="tagline__band tagline__band--teal">tragic moments</div>
      <div class="tagline__band tagline__band--slate">magic moments</div>
    </div>

    <a class="join-button" href="#join">
      <svg width="208" height="74" viewBox="0 0 208 74">
        <polygon points="0,8 208,0 178,74 4,70" fill="var(--join-blue)"/>
      </svg>
      <span>Join us</span>
    </a>
  </header>
</body>
</html>
```